Harbourline construction company Business card design

I need a business card design for my company. I have a logo but dont have business cards with our logo..

www.harbourlineconstructco.com.au

The logo is on the website

I need the same details as this design I have attached. we have changed the logo and colours. just like the website

Industry/Entity Type

Building

```html
<!DOCTYPE html>
<html lang="en">
<head>
<meta charset="utf-8">
<title>Harbourline Construction – Business Card</title>
<link rel="stylesheet" href="https://fonts.googleapis.com/css2?family=Tinos&display=swap">
<style>
  :root {
    --page-bg: #ffffff;
    --brand-blue: #31a7ef;
    --brand-grey: #bdcbcd;
    --text-light: #ffffff;
  }
  html, body {
    margin: 0;
    padding: 0;
    width: 1200px;
    height: 1000px;
    overflow: hidden;
    background: var(--page-bg);
  }
  .card {
    position: relative;
    width: 1200px;
    height: 1000px;
    font-family: "Tinos", "Times New Roman", serif;
  }
  .card-background {
    position: absolute;
    inset: 0;
  }
  .brand {
    position: absolute;
    left: 300px;
    top: 238px;
    display: flex;
    align-items: center;
    gap: 34px;
  }
  .brand-square {
    width: 62px;
    height: 62px;
    background: var(--brand-blue);
  }
  .brand-name {
    margin: 0;
    color: var(--brand-blue);
    font-size: 40px;
    font-weight: 400;
    letter-spacing: 7px;
    line-height: 46px;
    text-transform: uppercase;
  }
  .holder-name {
    position: absolute;
    left: 0;
    width: 1200px;
    top: 410px;
    margin: 0;
    text-align: center;
    font-size: 46px;
    font-weight: 400;
    color: var(--text-light);
    line-height: 56px;
  }
  .holder-name span {
    display: inline-block;
    padding: 0 8px;
    border-bottom: 2px solid var(--text-light);
  }
  .contact {
    position: absolute;
    left: 0;
    width: 1200px;
    top: 550px;
    margin: 0;
    text-align: center;
    font-style: normal;
    font-size: 27px;
    line-height: 37px;
    color: var(--text-light);
  }
</style>
</head>
<body>
  <main class="card">
    <svg class="card-background" width="1200" height="1000" viewBox="0 0 1200 1000" aria-hidden="true">
      <polygon class="panel-blue" points="68,205 256,358 600,358 600,795 68,795" fill="var(--brand-blue)"/>
      <polygon class="panel-grey" points="600,358 944,358 1132,205 1132,795 600,795" fill="var(--brand-grey)"/>
    </svg>

    <div class="brand">
      <div class="brand-square"></div>
      <p class="brand-name">Harbourline<br>Construction</p>
    </div>

    <h1 class="holder-name"><span>Name</span></h1>

    <address class="contact">
      Address :<br>
      Unit 4 Level 2, 18 Kestrel Pde,<br>
      Mindarie, WA 6030<br>
      Phone : 9381 2275 - Mob : 0422513906 ( Mai )<br>
      Email : info@harbourlineconstructco.com.au<br>
      www.harbourlineconstructco.com.au
    </address>
  </main>
</body>
</html>
```